Penwick Foot & Ankle Martinsburg Window Vinyl Cling

Hi,
I'm looking to get a window decal done, but need it professionally designed.
-must be 24" x 24"
-Quorum Font
-Include our logo, Podiatry, phone number and website
- The goal is to make this eye catching.
Thank you,
Warren

```html
<!DOCTYPE html>
<html lang="en">
<head>
<meta charset="utf-8">
<title>Penwick Foot &amp; Ankle – Window Cling</title>
<link rel="stylesheet" href="https://fonts.googleapis.com/css2?family=Roboto+Slab:wght@700&family=Montserrat:wght@700;800&display=swap">
<style>
  :root {
    --backdrop: #5c5c5c;
    --panel-dark: #232323;
    --panel-glow: #4a4a4a;
    --orange: #f07c45;
    --teal: #52c2a4;
    --teal-deep: #25866d;
    --white: #ffffff;
    --ink: #1f1f1f;
  }
  html, body {
    margin: 0;
    padding: 0;
    width: 1200px;
    height: 2400px;
    overflow: hidden;
    background: var(--backdrop);
  }
  .window-cling {
    position: absolute;
    left: 60px;
    top: 660px;
    width: 1080px;
    height: 1080px;
    display: block;
    box-shadow: 0 10px 30px rgba(0,0,0,0.35);
  }
  .slab { font-family: "Roboto Slab", Georgia, serif; font-weight: 700; }
  .sans { font-family: "Montserrat", Arial, sans-serif; }
  .brand-name { fill: var(--orange); }
  .brand-dot { fill: var(--teal); }
  .headline-podiatry { fill: var(--orange); stroke: var(--white); stroke-width: 2.5; paint-order: stroke; }
  .headline-specialty { fill: var(--teal); stroke: var(--white); stroke-width: 2; paint-order: stroke; }
  .headline-physicians { fill: var(--white); font-weight: 800; stroke: var(--teal); stroke-width: 1.5; paint-order: stroke; }
  .phone-pill { fill: var(--orange); stroke: var(--white); stroke-width: 2; }
  .phone-badge { fill: var(--ink); }
  .phone-glyph { fill: var(--orange); }
  .phone-number { fill: var(--white); font-weight: 700; }
  .footer-band-outer { fill: var(--teal-deep); }
  .footer-band-inner { fill: var(--teal); }
  .website { fill: var(--white); }
</style>
</head>
<body>
<svg class="window-cling" viewBox="0 0 968 968" xmlns="http://www.w3.org/2000/svg" role="group" aria-label="Penwick Foot and Ankle window cling">
  <defs>
    <radialGradient id="panel-glow" cx="484" cy="360" r="560" gradientUnits="userSpaceOnUse">
      <stop offset="0" stop-color="var(--panel-glow)"/>
      <stop offset="0.55" stop-color="#2d2d2d"/>
      <stop offset="1" stop-color="var(--panel-dark)"/>
    </radialGradient>
  </defs>

  <rect class="panel" width="968" height="968" fill="url(#panel-glow)"/>

  <g class="brand-lockup">
    <circle class="brand-dot" cx="190" cy="142" r="44"/>
    <text class="slab brand-name" x="260" y="162" font-size="54" textLength="570" lengthAdjust="spacingAndGlyphs">PENWICK FOOT &amp; ANKLE</text>
  </g>

  <text class="slab headline-podiatry" x="42" y="438" font-size="178" textLength="883" lengthAdjust="spacingAndGlyphs">PODIATRY</text>
  <text class="slab headline-specialty" x="66" y="548" font-size="112" textLength="838" lengthAdjust="spacingAndGlyphs">FOOT &amp; ANKLE</text>
  <text class="sans headline-physicians" x="146" y="648" font-size="92" textLength="678" lengthAdjust="spacingAndGlyphs">PHYSICIANS</text>

  <g class="phone-bar">
    <rect class="phone-pill" x="60" y="702" width="828" height="110" rx="24"/>
    <circle class="phone-badge" cx="128" cy="757" r="40"/>
    <path class="phone-glyph" d="M112 738c3-3 7-3 9 0l6 8c2 3 1 6-1 8l-3 3c3 6 8 11 14 14l3-3c2-2 5-3 8-1l8 6c3 2 3 6 0 9l-4 4c-4 4-10 4-16 1-11-6-20-15-26-26-3-6-3-12 1-16z"/>
    <text class="sans phone-number" x="200" y="792" font-size="94" textLength="650" lengthAdjust="spacingAndGlyphs">(555)214-0396</text>
  </g>

  <g class="footer-band">
    <path class="footer-band-outer" d="M0 968 V900 Q120 812 300 812 H668 Q848 812 968 900 V968 Z"/>
    <path class="footer-band-inner" d="M8 968 Q110 826 484 816 Q858 826 942 968 Z"/>
    <text class="slab website" x="105" y="925" font-size="70" textLength="740" lengthAdjust="spacingAndGlyphs">www.StepWellFeet.com</text>
  </g>
</svg>
</body>
</html>
```